Boutique Technology Consultancy specialising is Electronic and physical security

We need to redo our existing outdated website. For your reference the link www.brivo.com.au

```html
<!DOCTYPE html>
<html lang="en">
<head>
<meta charset="utf-8">
<title>Vantor Services</title>
<link href="https://fonts.googleapis.com/css2?family=Poppins:wght@400;500;600;700;800&display=swap" rel="stylesheet">
<style>
:root{
  --red:#c8201f;
  --red-dark:#a9191a;
  --ink:#1b1b1b;
  --grey:#555;
  --pink:#fcf2f2;
  --white:#fff;
  --black:#0d0d0d;
}
*{box-sizing:border-box;margin:0;padding:0}
html,body{width:1200px;height:5046px;overflow:hidden}
body{position:relative;font-family:"Poppins",sans-serif;color:var(--ink);background:var(--white)}
.abs{position:absolute}
.btn{position:absolute;display:flex;align-items:center;justify-content:center;gap:8px;background:var(--red);color:var(--white);font-weight:600;font-size:15px;border-radius:4px}
.btn.light{background:var(--white);color:var(--ink)}
.btn .dot{width:13px;height:13px;border-radius:50%;background:currentColor;position:relative}
.btn .dot::after{content:"";position:absolute;left:4px;top:3px;border-left:5px solid var(--red);border-top:3.5px solid transparent;border-bottom:3.5px solid transparent}
.btn.light .dot::after{border-left-color:var(--white)}
.title{position:absolute;left:0;width:1200px;display:flex;justify-content:center;align-items:center;gap:22px;font-weight:700;font-size:35px}
.title::before,.title::after{content:"";width:84px;height:2px;background:var(--red)}
.title.on-red{color:var(--white)}
.title.on-red::before,.title.on-red::after{background:var(--white)}

/* header / hero */
.hero-bg{left:0;top:0;width:1200px;height:720px;background:linear-gradient(100deg,#5d6b7d 0%,#8c9bb0 40%,#c4cfdc 75%,#dfe5ec 100%)}
.brand{position:absolute;display:flex;align-items:center;gap:10px;color:var(--white)}
.brand .mark{width:34px;height:34px;border-radius:50%;background:var(--red)}
.brand .name{font-weight:700;font-size:46px;line-height:1;letter-spacing:1px}
.brand .sub{font-size:13px;letter-spacing:7px;text-align:center;margin-top:2px}
.nav{left:450px;top:28px;display:flex;gap:30px;color:var(--white);font-size:15px;font-weight:500}
.hero-bar{left:117px;top:183px;width:8px;height:120px;background:var(--red)}
.hero-title{left:150px;top:168px;font-size:52px;font-weight:800;line-height:65px;color:var(--white);text-shadow:0 2px 6px rgba(0,0,0,.25)}
.hero-title .accent{color:var(--red);text-shadow:none}

/* about */
.about-head{left:111px;top:770px;font-size:35px;font-weight:700;display:flex;align-items:center;gap:10px}
.about-head::after{content:"";width:84px;height:2px;background:var(--red)}
.about-text{left:111px;top:828px;width:450px;font-size:15px;font-weight:600;line-height:27px}
.ticks{left:111px;top:937px;list-style:none;font-size:14px;color:var(--grey)}
.ticks li{display:flex;align-items:center;gap:8px;height:43px}
.ticks li::before{content:"";width:12px;height:12px;border-radius:50%;background:var(--red)}
.about-frame{left:593px;top:783px;width:478px;height:340px;border:3px solid var(--red);border-radius:6px}
.about-photo{left:607px;top:769px;width:476px;height:337px;background:linear-gradient(135deg,#3d4046,#8a8377 55%,#c9b39a);border-radius:4px}

/* services */
.services-bg{left:0;top:1247px;width:1200px;height:900px;background:var(--pink)}
.lead{position:absolute;left:0;width:1200px;text-align:center;font-size:14px;color:#333;line-height:23px}
.service{position:absolute;width:190px;text-align:center;font-size:14px;font-weight:600}
.service svg{display:block;margin:0 auto 14px}

/* experience */
.card{position:absolute;top:2339px;width:222px;height:255px;background:var(--white);border-radius:5px;text-align:center;box-shadow:0 3px 10px rgba(0,0,0,.15)}
.card .pic{margin:6px;height:146px;border-radius:3px}
.card h4{color:var(--red);font-size:14px;font-weight:600;margin-top:4px}
.card p{font-size:13px;color:var(--grey);line-height:23px;margin-top:4px}
.card .go{position:absolute;left:50%;bottom:-4px;transform:translateX(-50%);width:26px;height:26px;border-radius:50%;border:1.5px solid #333;background:var(--white)}
.card .go::after{content:"";position:absolute;left:10px;top:7px;border-left:7px solid #333;border-top:5px solid transparent;border-bottom:5px solid transparent}

/* team */
.member{position:absolute;top:2950px;width:274px;text-align:center}
.member .pic{height:368px;border-radius:2px}
.member h3{margin-top:22px;font-size:20px;font-weight:700;line-height:27px}
.social-stack{position:absolute;left:0;top:0;width:100%;height:368px;display:flex;flex-direction:column;align-items:center;justify-content:center;gap:44px}
.social-stack span{width:30px;height:30px;border-radius:50%;background:var(--white)}

/* offices */
.map{left:0;top:3592px;width:1200px;height:548px;background:linear-gradient(120deg,#e6e2d8,#d9dde4 60%,#b9d3e8)}
.office{position:absolute;color:var(--white);text-align:center;font-size:15px;line-height:21px}
.office h5{font-size:15px;font-weight:700;margin-bottom:14px}
.office .u{text-decoration:underline}

/* form */
.field{position:absolute;height:42px;border:1.5px solid #aaa;border-radius:5px;padding-left:20px;display:flex;align-items:center;font-size:14px;color:#555;background:var(--white)}

/* footer */
.foot-col{position:absolute;top:4755px;font-size:14px;color:var(--white);line-height:23px}
.foot-col h6{font-size:15px;font-weight:600;text-decoration:underline;margin-bottom:12px}
.foot-col p{margin-bottom:22px}
.sub-input{width:204px;height:38px;background:var(--white);border-radius:5px;color:#333;display:flex;align-items:center;padding-left:14px;font-size:13px;position:relative;margin-top:10px}
.sub-input i{position:absolute;right:4px;top:4px;width:30px;height:30px;border-radius:50%;background:var(--red)}
.foot-social{display:flex;gap:28px;margin-top:22px}
.foot-social span{width:16px;height:16px;border-radius:50%;background:var(--white)}
</style>
</head>
<body>

<!-- HERO -->
<div class="abs hero-bg" role="img" aria-label="Hand touching a glowing smart building network interface"></div>
<svg class="abs" style="left:0;top:520px" width="1200" height="240" viewBox="0 0 1200 240"><path d="M0 175 C200 150 380 70 560 45 C760 20 980 90 1200 60 L1200 240 L0 240 Z" fill="#fff"/></svg>

<div class="brand" style="left:108px;top:16px">
  <span class="mark"></span>
  <div><div class="name">VANTOR</div><div class="sub">SERVICES</div></div>
</div>
<nav class="abs nav"><span>Welcome</span><span>Experience</span><span>Services</span><span>Team</span><span>About</span></nav>
<div class="btn" style="left:924px;top:20px;width:160px;height:43px">Contact Us <span class="dot" style="background:#fff"></span></div>

<div class="abs hero-bar"></div>
<h1 class="abs hero-title">YOUR<br>TECHNOLOGY<br><span class="accent">PROJECTS MADE</span><br>EASY.</h1>
<div class="btn" style="left:148px;top:460px;width:162px;height:43px">Get In Touch <span class="dot" style="background:#fff"></span></div>

<!-- ABOUT -->
<h2 class="abs about-head">About Us</h2>
<p class="abs about-text">Vantor Services was established in 2016 by Ross Kellan to provide technology consulting services to corporate and government clients with a focus on:</p>
<ul class="abs ticks"><li>Property/facilities management</li><li>Asset management</li><li>Development and Construction</li></ul>
<div class="btn" style="left:111px;top:1080px;width:162px;height:44px">View More <span class="dot" style="background:#fff"></span></div>
<svg class="abs" style="left:610px;top:655px" width="150" height="130"><polygon points="140,0 150,120 0,115" fill="#c8201f"/><polygon points="140,0 150,120 90,110" fill="#8e1414"/></svg>
<div class="abs about-frame"></div>
<div class="abs about-photo" role="img" aria-label="Two consultants meeting over a laptop"></div>

<!-- SERVICES -->
<div class="abs services-bg"></div>
<h2 class="title" style="top:1330px">Our Services</h2>
<p class="lead" style="top:1400px">Vantor's services cover a broad range of technologies including</p>

<svg width="0" height="0" style="position:absolute"><defs>
<g id="tri"><polygon points="20,95 85,8 150,95" fill="#f3d8d8" transform="translate(-18,-6)"/><polygon points="0,90 78,0 156,90" fill="#c8201f"/></g>
</defs></svg>

<div class="service" style="left:107px;top:1468px"><svg width="160" height="92"><use href="#tri"/><circle cx="78" cy="58" r="16" fill="none" stroke="#fff" stroke-width="3"/></svg>Smart Buildings</div>
<div class="service" style="left:308px;top:1468px"><svg width="160" height="92"><use href="#tri"/><circle cx="78" cy="58" r="16" fill="none" stroke="#fff" stroke-width="3"/><circle cx="78" cy="58" r="5" fill="#fff"/></svg>Systems Integration</div>
<div class="service" style="left:510px;top:1468px"><svg width="160" height="92"><use href="#tri"/><rect x="64" y="40" width="28" height="36" rx="3" fill="none" stroke="#fff" stroke-width="3"/></svg>Control Centres</div>
<div class="service" style="left:711px;top:1468px"><svg width="160" height="92"><use href="#tri"/><rect x="58" y="42" width="40" height="8" fill="#fff"/><circle cx="78" cy="62" r="11" fill="none" stroke="#fff" stroke-width="3"/></svg>CCTV</div>
<div class="service" style="left:913px;top:1468px"><svg width="160" height="92"><use href="#tri"/><rect x="66" y="42" width="24" height="32" rx="4" fill="none" stroke="#fff" stroke-width="3"/><circle cx="78" cy="56" r="4" fill="#fff"/></svg>Access Control</div>

<div class="service" style="left:107px;top:1713px"><svg width="160" height="92"><use href="#tri"/><rect x="58" y="46" width="38" height="26" rx="3" fill="none" stroke="#fff" stroke-width="3"/></svg>Smart Cards</div>
<div class="service" style="left:308px;top:1713px"><svg width="160" height="92"><use href="#tri"/><path d="M68 52 v-8 a10 10 0 0 1 20 0 v8" fill="none" stroke="#fff" stroke-width="3"/><rect x="63" y="52" width="30" height="24" rx="3" fill="none" stroke="#fff" stroke-width="3"/></svg>Electronic Lockers</div>
<div class="service" style="left:510px;top:1713px"><svg width="160" height="92"><use href="#tri"/><rect x="62" y="42" width="32" height="32" rx="3" fill="none" stroke="#fff" stroke-width="3"/><path d="M70 66 l8-14 8 14z" fill="#fff"/></svg>Intruder Alarms</div>
<div class="service" style="left:711px;top:1713px"><svg width="160" height="92"><use href="#tri"/><path d="M66 70 h24 l-3-5 v-10 a9 9 0 0 0-18 0 v10z" fill="none" stroke="#fff" stroke-width="3"/><circle cx="78" cy="74" r="3" fill="#fff"/></svg>Staff Safety Alarms</div>
<div class="service" style="left:913px;top:1713px"><svg width="160" height="92"><use href="#tri"/><path d="M60 52 a26 26 0 0 1 36 0 M66 59 a17 17 0 0 1 24 0 M72 66 a8 8 0 0 1 12 0" fill="none" stroke="#fff" stroke-width="3.5" stroke-linecap="round"/><circle cx="78" cy="72" r="3.5" fill="#fff"/></svg>Wi-Fi</div>

<div class="btn" style="left:519px;top:1943px;width:161px;height:43px">View More <span class="dot" style="background:#fff"></span></div>

<!-- EXPERIENCE -->
<svg class="abs" style="left:0;top:2010px" width="1200" height="800" viewBox="0 0 1200 800"><path d="M0 95 C300 80 520 55 760 50 C950 45 1080 25 1200 15 L1200 710 C950 745 700 730 450 760 C250 780 120 790 0 780 Z" fill="#c8201f"/></svg>
<h2 class="title on-red" style="top:2180px">Our Experience</h2>
<p class="lead" style="top:2250px;color:#fff">Vantor has a diverse range of project experience across a range of industries within both the public and<br>private sectors. The following is a small sample of some of the clients and sites we have worked with.</p>

<div class="card" style="left:118px"><div class="pic" role="img" aria-label="Glass dome atrium of a shopping centre" style="background:linear-gradient(160deg,#2b2b2b,#9a9a9a)"></div><h4>Harbourline Plaza</h4><p>Security technology<br>design consulting for</p><span class="go"></span></div>
<div class="card" style="left:366px"><div class="pic" role="img" aria-label="Glass office towers against the sky" style="background:linear-gradient(160deg,#8fb3d8,#4f6c8a)"></div><h4>Meridian Towers</h4><p>Shared building<br>network and security</p><span class="go"></span></div>
<div class="card" style="left:613px"><div class="pic" role="img" aria-label="Waterfront bank headquarters building" style="background:linear-gradient(170deg,#9a7d55,#c7a26c 55%,#5a5a52)"></div><h4>Southern Federal<br>Bank</h4><p>Security operations</p><span class="go" style="border-color:#c8201f"></span></div>
<div class="card" style="left:861px"><div class="pic" role="img" aria-label="Aerial view of a water treatment site" style="background:linear-gradient(170deg,#5c7a88,#3f6b44 60%,#6a7f6a)"></div><h4>Riverbend Water</h4><p>Critical infrastructure<br>Security Upgrade for</p><span class="go"></span></div>

<div class="btn light" style="left:519px;top:2642px;width:161px;height:44px">View More <span class="dot"></span></div>

<!-- TEAM -->
<svg class="abs" style="left:0;top:2815px" width="460" height="510"><polygon points="55,0 260,150 0,505" fill="#c8201f"/><polygon points="395,255 455,290 395,330" fill="#c8201f"/></svg>
<h2 class="title" style="top:2850px">Our Team</h2>
<div class="member" style="left:114px"><div class="pic" role="img" aria-label="Portrait of the principal consultant" style="background:linear-gradient(180deg,#d8d8d8,#9a9a9a)"></div><h3>Graham Tolley - Principal<br>Consultant</h3></div>
<div class="member" style="left:460px"><div class="pic" role="img" aria-label="Portrait of a consultant with red overlay" style="background:linear-gradient(180deg,#c42424,#8e1616)"></div><div class="social-stack"><span></span><span></span><span></span></div><h3>Declan Rourke<br>Consultant</h3></div>
<div class="member" style="left:812px"><div class="pic" role="img" aria-label="Portrait of the operations coordinator" style="background:linear-gradient(180deg,#e6e6e6,#b8b8b8)"></div><h3>Mei Lanfort - Operations<br>and Administration<br>Coordinator</h3></div>
<div class="btn" style="left:519px;top:3439px;width:161px;height:42px">View More <span class="dot" style="background:#fff"></span></div>

<!-- OFFICES -->
<div class="abs map" role="img" aria-label="Street map of the city office area"></div>
<svg class="abs" style="left:0;top:3530px" width="1200" height="610"><polygon points="690,0 645,610 1200,420" fill="#c8201f"/></svg>
<div class="office" style="left:660px;top:3656px;width:180px"><h5>MELBOURNE OFFICE</h5>Ross Kellan<br><span class="u">0400 000 118</span><br><br><span class="u">Level 1, 212 Carden St,<br>Melbourne VIC 3000</span></div>
<div class="office" style="left:660px;top:3880px;width:160px"><h5>SYDNEY OFFICE</h5>Ned Varley<br>0400 000 245<br><br>17 Harlow St,<br>Sydney NSW 2000</div>
<div class="office" style="left:875px;top:3816px;width:200px"><h5>QUEENSLAND OFFICE</h5>Peter Ashby<br>0400 000 372<br><br>45 Tallis Street,<br>Brisbane QLD 4000</div>

<!-- CONTACT FORM -->
<h2 class="title" style="top:4215px">Get In Touch</h2>
<div class="field" style="left:127px;top:4307px;width:259px">Name</div>
<div class="field" style="left:470px;top:4307px;width:259px">Email</div>
<div class="field" style="left:812px;top:4307px;width:259px">Phone</div>
<div class="field" style="left:127px;top:4376px;width:259px">Subject</div>
<div class="field" style="left:470px;top:4376px;width:601px">Message</div>
<div class="btn" style="left:519px;top:4442px;width:161px;height:44px">Submit</div>

<!-- FOOTER -->
<svg class="abs" style="left:0;top:4520px" width="1200" height="526" viewBox="0 0 1200 526"><path d="M0 30 C250 70 500 20 760 40 C950 55 1080 35 1200 45 L1200 526 L0 526 Z" fill="#0d0d0d"/></svg>
<div class="brand" style="left:113px;top:4650px">
  <span class="mark"></span>
  <div><div class="name">VANTOR</div><div class="sub">SERVICES</div></div>
</div>
<div class="foot-col" style="left:121px;width:300px"><p>Victorian Private Security Business Registration Number: 000-111-22S</p><p>Queensland Security Firm License Number: 4000123</p><p>New South Wales Master Security Licence Number: 000100456</p></div>
<div class="foot-col" style="left:451px"><h6>Quick Links</h6>Home<br>Service<br>Experience<br>About Us<br>Projects</div>
<div class="foot-col" style="left:606px"><h6>Contact Us</h6>Level 2,<br>212 Carden Street Melbourne,<br>VIC, 3000AUSTRALIA<br>1300 000 555<br>HELLO@VANTOR.COM.AU</div>
<div class="foot-col" style="left:881px"><h6>Subscribe</h6>Subscribe To Our Newsletter<div class="sub-input">Enter Email<i></i></div><div class="foot-social"><span></span><span></span><span></span></div></div>
<div class="abs" style="left:0;top:4988px;width:1200px;text-align:center;color:#fff;font-size:12px">Copyright@2023. All Rights Reserved by VANTOR SERVICES</div>

</body>
</html>
```